Start up business website

IT Support provider that caters towards law enforcement / police departments. We'll offer remote IT support, backup / recovery services and cyber security. Will add updates soon.

Target Market(s)

Police departments / Law Enforcement

Coding

Coded - Design and coding required

Number of Pages Required

5+ page

Font styles to use
Other font styles liked:
• Use font style in uploaded logo

Colors
0054AA
0677BA
7BADD7
CADEEF
E8F1F8

```html
<!DOCTYPE html>
<html lang="en">
<head>
<meta charset="utf-8">
<title>Bastion Support Services</title>
<link rel="stylesheet" href="https://fonts.googleapis.com/css2?family=Outfit:wght@300;400;500;600;700&display=swap">
<style>
:root{
  --brand:#2f55ab;
  --brand-deep:#0054aa;
  --accent:#0677ba;
  --sky:#7badd7;
  --mist:#cadeef;
  --ice:#e8f1f8;
  --navy:#0e3358;
  --navy-cell:#154a78;
  --ink:#1b1b1b;
  --muted:#555;
  --white:#fff;
}
*{box-sizing:border-box;margin:0;padding:0}
html,body{width:1200px;height:2881px;overflow:hidden}
body{font-family:"Outfit",sans-serif;color:var(--ink);background:var(--white);position:relative}
.abs{position:absolute}
a{color:inherit;text-decoration:none}

/* header */
.hero{left:0;top:0;width:1200px;height:653px;background:linear-gradient(180deg,#fff 0%,#f4f5f7 55%,#e4e6ea 100%);overflow:hidden}
.brand-name{left:192px;top:42px;font-size:26px;font-weight:700;color:var(--brand-deep);letter-spacing:.5px;display:flex;align-items:center;gap:10px}
.brand-name .mark{width:30px;height:30px;border-radius:50%;background:var(--brand-deep)}
.topline{top:12px;right:215px;font-size:12px;color:#333;display:flex;gap:18px;align-items:center}
.topline span{display:flex;align-items:center;gap:6px}
.nav{left:454px;top:41px;width:746px;height:38px;background:var(--brand);border-radius:19px 0 0 19px;display:flex;align-items:center;padding-left:46px;gap:25px}
.nav a{color:#fff;font-size:12.5px;letter-spacing:.2px}
.hero-photo{left:643px;top:78px;width:557px;height:575px;background:radial-gradient(ellipse at 70% 40%,#2c4f86 0%,#10203f 55%,#0a1428 100%);border-radius:70% 0 0 0 / 40% 0 0 0}
.dots{left:108px;top:268px;width:16px}
.hero-sub{left:194px;top:264px;font-size:32px;font-weight:400;color:#222}
.hero-title{left:194px;top:309px;font-size:42px;font-weight:600;color:#222}
.btn{display:inline-flex;align-items:center;justify-content:center;background:var(--brand);color:#fff;border-radius:20px;font-weight:500}
.hero-btn{left:194px;top:389px;width:173px;height:37px;font-size:14px}

/* services */
.services{left:0;top:653px;width:1200px;height:600px;background:linear-gradient(180deg,var(--brand) 0%,#2d54a9 70%,#3d63b4 100%)}
.card{width:187px;height:177px;background:#fff;padding:6px}
.card-inner{width:100%;height:100%;border:1px solid #d4d4d4;border-radius:3px;text-align:center;padding-top:18px}
.card h3{font-size:15px;font-weight:600;line-height:19px;color:#222}
.card .bar{width:34px;height:3px;background:var(--accent);margin:12px auto 16px}
.card p{font-size:10.5px;line-height:16px;color:#666;padding:0 18px}
.pitch{left:693px;top:810px;color:#b9c8e6;font-size:38px;line-height:46px;font-weight:300}
.pitch strong{display:block;color:#fff;font-weight:700;font-size:44px;line-height:50px;margin-top:4px}
.pitch small{display:block;font-size:22px;line-height:35px;font-weight:300;margin-top:14px}

/* about */
.about{left:0;top:1253px;width:1200px;height:546px;background:linear-gradient(180deg,#fff 0%,#f6f7f9 60%,#eceef1 100%)}
.about-photo{left:227px;top:1345px;width:350px;height:350px;border-radius:26px;background:linear-gradient(135deg,#3a5f8f 0%,#1e3a63 45%,#cfcac2 100%)}
.about-frame{left:239px;top:1357px;width:326px;height:326px;border:1px solid rgba(255,255,255,.55);border-radius:20px}
.about h2{}
.about-title{left:657px;top:1372px;font-size:27px;font-weight:600}
.about-lead{left:657px;top:1420px;width:330px;font-size:15px;line-height:21px}
.about-copy{left:657px;top:1473px;width:320px;font-size:11.5px;line-height:23px;color:#555}
.about-btn{left:657px;top:1624px;width:123px;height:38px;font-size:13px}

/* outcomes */
.outcomes{left:0;top:1799px;width:1200px;height:741px;background:linear-gradient(180deg,var(--navy) 0%,#103a63 70%,#18497a 100%)}
.outcomes-title{left:230px;top:1880px;font-size:40px;line-height:52px;color:#fff;font-weight:400}
.outcomes-title b{font-weight:500}
.cell-hl{left:496px;top:2037px;width:276px;height:189px;background:var(--navy-cell)}
.outcome{width:250px;color:#fff}
.outcome svg{display:block;margin-bottom:30px}
.outcome h4{font-size:20px;line-height:24px;font-weight:500}
.rule-h{left:231px;top:2226px;width:806px;height:1px;background:rgba(255,255,255,.18)}
.rule-v{width:1px;background:rgba(255,255,255,.18)}
.knot{width:9px;height:9px;border-radius:50%;background:#2e6aa0}

/* footer */
.footer{left:0;top:2540px;width:1200px;height:341px;background:#f7f7f7}
.foot-brand{left:195px;top:2628px;font-size:20px;font-weight:700;color:var(--brand-deep);display:flex;align-items:center;gap:8px}
.foot-brand .mark{width:24px;height:24px;border-radius:50%;background:var(--brand-deep)}
.foot-about{left:194px;top:2692px;width:175px;font-size:11px;line-height:19px;color:#444}
.fdiv{top:2597px;width:1px;height:181px;background:#ddd}
.fhead{font-size:16px;color:#333}
.fhead::before{content:"";display:block;width:30px;height:2px;background:var(--brand);margin-bottom:13px}
.flinks{font-size:11.5px;line-height:20px;color:#444;list-style:none}
.contact-row{display:flex;gap:10px;font-size:11.5px;line-height:16px;color:#444}
.social{display:flex;gap:6px}
.social span{width:22px;height:22px;border-radius:50%;background:var(--brand)}
.news{left:871px;top:2751px;width:146px;height:27px;display:flex}
.news .field{flex:1;background:#fff;font-size:9px;color:#999;padding:9px 10px}
.news .send{width:27px;background:var(--brand);display:flex;align-items:center;justify-content:center}
.legal{top:2842px;font-size:11.5px;color:#333}
</style>
</head>
<body>

<section class="abs hero" aria-label="Welcome">
  <div class="abs hero-photo" role="img" aria-label="Profile silhouette merged with a night city skyline and technicians at screens"></div>
</section>

<div class="abs brand-name"><span class="mark"></span>BASTION</div>
<div class="abs topline">
  <span><svg width="9" height="13" viewBox="0 0 9 13"><rect x=".5" y=".5" width="8" height="12" rx="1.5" fill="none" stroke="#333"/></svg>+1 555 014 2290</span>
  <span><svg width="14" height="10" viewBox="0 0 14 10"><rect x=".5" y=".5" width="13" height="9" fill="none" stroke="#333"/><path d="M.5 .5 7 5.5 13.5 .5" fill="none" stroke="#333"/></svg>hello@bastionsupport.example</span>
</div>
<nav class="abs nav">
  <a href="#">HOME</a><a href="#">SERVICES</a><a href="#">ABOUT US</a><a href="#">FOLLOW UP</a><a href="#">CJIS COMPLIANCE</a><a href="#">CONTACT US</a>
</nav>

<svg class="abs dots" width="16" height="60" viewBox="0 0 16 60">
  <circle cx="8" cy="8" r="7" fill="none" stroke="#0677ba" stroke-width="1.5"/><circle cx="8" cy="8" r="3.5" fill="#0677ba"/>
  <circle cx="8" cy="28" r="3.5" fill="#0677ba"/><circle cx="8" cy="41" r="3.5" fill="#0677ba"/><circle cx="8" cy="54" r="3.5" fill="#0677ba"/>
</svg>
<p class="abs hero-sub">Collaborating to find solutions</p>
<h1 class="abs hero-title">For Any Challenge</h1>
<a class="abs btn hero-btn" href="#">Free Consultation</a>

<section class="abs services" aria-label="Services"></section>
<div class="abs card" style="left:219px;top:725px"><div class="card-inner"><h3>IT support</h3><div class="bar"></div><p>Lorem Ipsum is the simply dummy text of the printing and typesetting industry.</p></div></div>
<div class="abs card" style="left:444px;top:775px"><div class="card-inner"><h3>Backup / Recovery<br>Services</h3><div class="bar"></div><p>Lorem Ipsum is the simply dummy text of the printing and typesetting industry.</p></div></div>
<div class="abs card" style="left:219px;top:938px"><div class="card-inner"><h3>Cyber Security</h3><div class="bar"></div><p>Lorem Ipsum is the simply dummy text of the printing and typesetting industry.</p></div></div>
<div class="abs card" style="left:444px;top:988px"><div class="card-inner"><h3>Technology<br>Solutions</h3><div class="bar"></div><p>Lorem Ipsum is the simply dummy text of the printing and typesetting industry.</p></div></div>
<h2 class="abs pitch">Create New<br>Possiblities For<strong>Yourself And<br>Your Team.</strong><small>World Class Technology for<br>The Mordern Enterprisee.</small></h2>

<section class="abs about" aria-label="About"></section>
<div class="abs about-photo" role="img" aria-label="Technician holding an open laptop in a dim office"></div>
<div class="abs about-frame"></div>
<h2 class="abs about-title">About Us</h2>
<p class="abs about-lead">Lorem Ipsum is simply dummy text of the printing and typesetting industry.</p>
<p class="abs about-copy">Lorem Ipsum is simply dummy text of the printing and type-setting industry. Lorem Ipsum has been the industry's standard dummy text ever since the 1500s, when an unknown printer took a galley of type and scrambled it to make a type specimen book. It has survived not only five centuries.</p>
<a class="abs btn about-btn" href="#">Learn More</a>

<section class="abs outcomes" aria-label="Outcomes"></section>
<h2 class="abs outcomes-title">What Do You Wish to<br><b>Do better?</b></h2>
<div class="abs cell-hl"></div>
<div class="abs rule-h"></div>
<div class="abs rule-v" style="left:496px;top:2037px;height:378px"></div>
<div class="abs rule-v" style="left:772px;top:2037px;height:378px"></div>
<div class="abs knot" style="left:492px;top:2222px"></div>
<div class="abs knot" style="left:768px;top:2222px"></div>

<div class="abs outcome" style="left:231px;top:2058px">
  <svg width="58" height="58" viewBox="0 0 58 58" fill="none" stroke="#6fa8dc" stroke-width="1.6"><path d="M8 2l2 5h5l-4 3 2 5-5-3-5 3 2-5-4-3h5z"/><path d="M29 2l2 5h5l-4 3 2 5-5-3-5 3 2-5-4-3h5z"/><path d="M49 2l2 5h5l-4 3 2 5-5-3-5 3 2-5-4-3h5z"/><path d="M24 54V36c0-3 5-3 5 0v-14c0-3 5-3 5 0v18l6 2c3 1 3 5 2 8l-3 6"/></svg>
  <h4>Increase Customer<br>Satisfaction</h4>
</div>
<div class="abs outcome" style="left:533px;top:2058px">
  <svg width="58" height="58" viewBox="0 0 58 58" fill="none" stroke="#6fa8dc" stroke-width="1.6"><circle cx="29" cy="36" r="9"/><path d="M29 30v12M26 33h5a2 2 0 010 4h-4a2 2 0 000 4h5"/><path d="M8 50V24M8 24l-4 5M8 24l4 5M50 50V20M50 20l-4 5M50 20l4 5M29 20V4M29 4l-4 5M29 4l4 5M18 26V12M40 26V12"/></svg>
  <h4>Avoid Unnecessary<br>Costs</h4>
</div>
<div class="abs outcome" style="left:810px;top:2058px">
  <svg width="58" height="58" viewBox="0 0 58 58" fill="none" stroke="#6fa8dc" stroke-width="1.6"><circle cx="29" cy="38" r="15"/><circle cx="29" cy="38" r="11"/><path d="M23 38l4 4 8-8M29 23V2M2 38h12M44 38h12"/><circle cx="29" cy="2" r="1.5"/></svg>
  <h4>Improve<br>Efficiency</h4>
</div>
<div class="abs outcome" style="left:231px;top:2262px">
  <svg width="58" height="58" viewBox="0 0 58 58" fill="none" stroke="#6fa8dc" stroke-width="1.6"><circle cx="29" cy="16" r="12"/><path d="M29 9v7l5 3"/><path d="M4 14v22l12 14v6M54 14v22L42 50v6M10 24v12l8 8M48 24v12l-8 8"/></svg>
  <h4>Save Time &amp;<br>Effort</h4>
</div>
<div class="abs outcome" style="left:533px;top:2262px">
  <svg width="58" height="58" viewBox="0 0 58 58" fill="none" stroke="#6fa8dc" stroke-width="1.6"><rect x="2" y="2" width="54" height="54" rx="6"/><path d="M29 10l16 6v14c0 10-8 16-16 20-8-4-16-10-16-20V16z"/><path d="M22 30l5 5 9-9"/></svg>
  <h4>Build a More Secure<br>Environment</h4>
</div>
<div class="abs outcome" style="left:810px;top:2262px">
  <svg width="58" height="58" viewBox="0 0 58 58" fill="none" stroke="#6fa8dc" stroke-width="1.6"><circle cx="29" cy="30" r="22"/><path d="M20 32l9-9 9 9M23 30v10h12V30"/><circle cx="29" cy="6" r="4" fill="#0e3358"/><circle cx="8" cy="44" r="4" fill="#0e3358"/><circle cx="50" cy="44" r="4" fill="#0e3358"/></svg>
  <h4>Gain Visiblity &amp;<br>Control</h4>
</div>

<footer class="abs footer" aria-label="Footer"></footer>
<div class="abs foot-brand"><span class="mark"></span>BASTION</div>
<p class="abs foot-about">We take the time to understand our clients environment so that we can offer technology solutions that are flexible and robust.</p>
<div class="abs fdiv" style="left:392px"></div>
<div class="abs fdiv" style="left:560px"></div>
<div class="abs fdiv" style="left:815px"></div>

<div class="abs" style="left:446px;top:2598px">
  <h5 class="fhead">Site Links</h5>
  <ul class="flinks" style="margin-top:22px"><li>Home</li><li>Services</li><li>About</li><li>CJIS Compliance</li><li>Follow Up</li><li>Contact Us</li></ul>
</div>
<div class="abs" style="left:603px;top:2598px;width:190px">
  <h5 class="fhead">Contact Us</h5>
  <div class="contact-row" style="margin-top:24px"><svg width="14" height="14" viewBox="0 0 14 14" fill="none" stroke="#2f55ab"><path d="M3 1l2 3-1.5 1.5c1 2 3 4 5 5L10 9l3 2-1 2c-6 0-11-5-11-11z"/></svg>Phone: 555 017 3348</div>
  <div class="contact-row" style="margin-top:16px"><svg width="14" height="16" viewBox="0 0 14 16" fill="none" stroke="#2f55ab"><path d="M7 15s5-5 5-9A5 5 0 002 6c0 4 5 9 5 9z"/><circle cx="7" cy="6" r="2"/></svg>Address: 48 Harbor Lane, Suite 9, Riverton, NY</div>
  <div class="contact-row" style="margin-top:24px"><svg width="14" height="12" viewBox="0 0 14 12" fill="none" stroke="#2f55ab"><rect x=".5" y="1.5" width="13" height="10"/><path d="M.5 1.5 7 7l6.5-5.5"/></svg>Email: desk@bastionsupport.example</div>
</div>
<div class="abs" style="left:871px;top:2598px;width:152px">
  <h5 class="fhead">Get Connected</h5>
  <div class="social" style="margin-top:12px"><span></span><span></span><span></span></div>
  <div style="height:1px;background:#ddd;margin-top:14px"></div>
</div>
<div class="abs" style="left:871px;top:2701px"><h5 class="fhead">Newsletter</h5></div>
<div class="abs news"><div class="field">Email...</div><div class="send"><svg width="12" height="12" viewBox="0 0 12 12"><path d="M11 1 1 5l4 2 1 4z" fill="#fff"/></svg></div></div>

<p class="abs legal" style="left:182px">@2021 Bastion Support Services &nbsp;|&nbsp; All Rights Reserved.</p>
<p class="abs legal" style="right:179px">Terms &amp; Conditions &nbsp;|&nbsp; Privacy Policy</p>

</body>
</html>
```